1 Page Rate Sheet Designed in Word

I am looking for a superfast turn-around on a 1-page rate sheet for a small financial services company.
Logo and content supplied, simply needs professional formatting and added styling to make it stand out.
The sheet needs to be designed in Word so that it can be updated daily.

Some additional notes on attached content outline:

It needs to look professional - "bank-ish" but with the BLV appetite for a little flash.
You can see their website at www.blvlending.example
It's for brokers and loan wholesalers - not the general public.
Order of products should remain as is, the rates should be "the first thing people see".
I'm attaching the content here and also a sample of what a "real" rate sheet looks like. See "real" rate sheets here -
http://www.torvenfunding.example/RateSheets/SubPrimeCore3.0.pdf
http://online.qrdailyledger.example/public/resources/documents/retro_SubPrime1107.html

Please feel free to contact me for more information or clarification.
Updates

Please note, have just replaced the earlier version of the content document with an updated version.

Target Market(s)

Loan Brokers, Mortgage Wholesalers

Industry/Entity Type

Financial

Colors
34a7d8
00a98f

Requirements
Must have
• Experience in formatting and designing in Word.

```html
<!DOCTYPE html>
<html lang="en">
<head>
<meta charset="utf-8">
<title>BLV Lending Residential Rate Sheet</title>
<link rel="stylesheet" href="https://fonts.googleapis.com/css2?family=Arimo:wght@400;700&family=Arvo:wght@400;700&family=Montserrat:wght@500;600&family=Open+Sans:wght@700&display=swap">
<style>
  :root {
    --page-edge: #f3b46a;
    --header-blue: #5897d4;
    --band-green: #6aa842;
    --heading-green: #6aa842;
    --title-blue: #4a86c8;
    --table-line: #4472c4;
    --row-tint: #d3dff0;
    --ink: #1f1f1f;
    --white: #ffffff;
    --badge: #e8eef6;
  }
  * { margin: 0; padding: 0; box-sizing: border-box; }
  html, body { width: 951px; height: 1200px; overflow: hidden; background: #ffffff; }
  .canvas { position: relative; width: 951px; height: 1200px; }
  .page {
    position: absolute; left: 23px; top: 18px; width: 908px; height: 1176px;
    border: 1px solid var(--page-edge); background: var(--white);
    box-shadow: 3px 3px 6px rgba(0,0,0,0.25);
  }
  .masthead { position: absolute; left: 23px; top: 40px; width: 877px; height: 160px; }
  .masthead-blue { position: absolute; left: 0; top: 0; width: 100%; height: 129px; background: var(--header-blue); }
  .masthead-green { position: absolute; left: 0; top: 129px; width: 100%; height: 31px; background: var(--band-green); }
  .brand-name {
    position: absolute; left: 34px; top: 82px;
    font-family: "Arimo", sans-serif; font-weight: 400; font-size: 30px; color: var(--white);
    letter-spacing: 1px; line-height: 34px;
  }
  .masthead-phone {
    position: absolute; right: 64px; top: 60px;
    font-family: "Arimo", sans-serif; font-size: 37px; color: var(--white); letter-spacing: 0.5px;
  }
  .section-heading {
    position: absolute; left: 0; width: 951px; top: 262px; text-align: center;
    font-family: "Arvo", serif; font-weight: 700; font-size: 27px; color: var(--heading-green);
    letter-spacing: 0.5px;
  }
  .program { position: absolute; left: 147px; width: 680px; }
  .program-title {
    font-family: "Open Sans", sans-serif; font-weight: 700; font-size: 15px; color: var(--title-blue);
    margin-left: 9px; line-height: 18px;
  }
  .program-desc {
    font-family: "Arimo", sans-serif; font-size: 10.5px; line-height: 13px; color: var(--ink);
    margin-left: 35px; width: 622px;
  }
  .rate-table {
    position: absolute; left: 147px; width: 532px; border-collapse: collapse;
  }
  .rate-table th, .rate-table td {
    border: 1px solid var(--table-line); height: 23px; width: 33.33%;
  }
  .rate-table th {
    font-family: "Arvo", serif; font-weight: 700; font-size: 15px; color: var(--ink);
    text-align: left; padding-left: 9px; background: var(--white); height: 24px;
  }
  .rate-table tbody tr:nth-child(odd) td { background: var(--row-tint); }
  .footer {
    position: absolute; left: 57px; top: 1009px; width: 871px; height: 159px; background: var(--header-blue);
    font-family: "Montserrat", sans-serif; font-weight: 500; font-size: 18px; color: var(--white);
    text-align: center;
  }
  .footer-line { position: absolute; left: 0; width: 100%; line-height: 24px; }
  .footer-line.address { top: 49px; }
  .footer-line.contact { top: 74px; }
  .badges { position: absolute; left: 608px; top: 100px; display: flex; gap: 7px; align-items: center; }
  .badge { background: var(--badge); height: 12px; }
  .badge.wide { width: 40px; }
  .badge.square { width: 14px; height: 14px; }
  .badge.mid { width: 28px; }
</style>
</head>
<body>
<div class="canvas">
  <div class="page"></div>

  <header class="masthead">
    <div class="masthead-blue"></div>
    <div class="masthead-green"></div>
    <div class="brand-name">BLV Lending</div>
    <div class="masthead-phone">800-555-0142</div>
  </header>

  <h1 class="section-heading">RESIDENTIAL</h1>

  <section class="program" style="top:311px;">
    <h2 class="program-title">Foreign National Partnership Program</h2>
    <p class="program-desc">Foreign Nationals Only, Purchase or Refinance, Up to 75% LTV, Primary, 2nd Home or Investment.&nbsp; No Pre-Payment, 5 Year Balloon, Money Down must in US for 30 Days.</p>
  </section>
  <table class="rate-table" style="top:372px;">
    <thead><tr><th>Rate</th><th>Cost</th><th>Add-Ons or Fees</th></tr></thead>
    <tbody>
      <tr><td></td><td></td><td></td></tr>
      <tr><td></td><td></td><td></td></tr>
      <tr><td></td><td></td><td></td></tr>
      <tr><td></td><td></td><td></td></tr>
      <tr><td></td><td></td><td></td></tr>
      <tr><td></td><td></td><td></td></tr>
      <tr><td></td><td></td><td></td></tr>
    </tbody>
  </table>

  <section class="program" style="top:625px;">
    <h2 class="program-title">Inherited Property Program</h2>
    <p class="program-desc">Up To 80% LTV &amp; Up To 5 Year Term, No Minimum Credit Score, Future Value of Rental Income Considered, Bankruptcy, Foreclosure &amp; Short Sales Are Ok, Deferred Maintenance Acceptable, Debt Consolidation Allowed, Rehab Money Escrow for Future Value to Sell Available, Refinancing of Reverse Mortgages Available.</p>
  </section>
  <table class="rate-table" style="top:699px;">
    <thead><tr><th>Rate</th><th>Cost</th><th>Add-Ons or Fees</th></tr></thead>
    <tbody>
      <tr><td></td><td></td><td></td></tr>
      <tr><td></td><td></td><td></td></tr>
      <tr><td></td><td></td><td></td></tr>
      <tr><td></td><td></td><td></td></tr>
      <tr><td></td><td></td><td></td></tr>
      <tr><td></td><td></td><td></td></tr>
      <tr><td></td><td></td><td></td></tr>
    </tbody>
  </table>

  <footer class="footer">
    <p class="footer-line address">415 Larkmoor Avenue,&nbsp; Suite 6, Glenford, MD 20850&nbsp; |&nbsp; www.blvlending.example</p>
    <p class="footer-line contact">Direct: 800-555-0142&nbsp; Evenings &amp; Weekends: 877-555-0187</p>
    <div class="badges" aria-label="Industry membership badges">
      <span class="badge wide"></span>
      <span class="badge square"></span>
      <span class="badge mid"></span>
    </div>
  </footer>
</div>
</body>
</html>
```